Email Signature

I would like an email signature that includes all 5 of my companies.

At the moment I just have a list of all 5 companies but that is too dull. Naturally, I would like it to be not too big but to clearly show all 5 companies.

Thanks

```html
<!DOCTYPE html>
<html lang="en">
<head>
<meta charset="utf-8">
<title>Email Signature</title>
<link rel="stylesheet" href="https://fonts.googleapis.com/css2?family=Arimo:wght@400;700&display=swap">
<style>
  :root {
    --ink-dark: #565a61;
    --ink-light: #b4b7bd;
    --ink-black: #111111;
    --frame: #222222;
    --paper: #ffffff;
    --divider: #5b5f66;
    --mascot-yellow: #f2c230;
    --mascot-blue: #3f8fd6;
    --mascot-grey: #9a9ca0;
    --mark-green: #8cc152;
    --mark-blue: #6fa8dc;
  }
  html, body {
    margin: 0;
    padding: 0;
    overflow: hidden;
    background: var(--paper);
  }
  .signature {
    position: relative;
    width: 1200px;
    height: 850px;
    box-sizing: border-box;
    border: 1px solid var(--frame);
    background: var(--paper);
    font-family: "Arimo", Arial, sans-serif;
    overflow: hidden;
  }
  .sign-off {
    position: absolute;
    left: 87px;
    top: 232px;
    margin: 0;
    font-size: 28px;
    color: var(--ink-light);
  }
  .details {
    position: absolute;
    left: 87px;
    top: 345px;
    margin: 0;
    font-style: normal;
  }
  .details .line {
    display: block;
    font-size: 28px;
    line-height: 38px;
    color: var(--ink-light);
    white-space: nowrap;
  }
  .details .name {
    font-size: 32px;
    font-weight: 700;
    color: var(--ink-dark);
  }
  .details .title {
    font-size: 27px;
    font-weight: 700;
    color: var(--ink-dark);
  }
  .details .label {
    font-weight: 700;
    color: var(--ink-dark);
  }
  .details .sep {
    font-weight: 700;
    color: var(--ink-dark);
    margin: 0 12px;
    font-size: 22px;
  }
  .mascot {
    position: absolute;
    top: 553px;
    width: 140px;
  }
  .mascot .art {
    display: block;
    width: 140px;
    height: 125px;
    border-radius: 10px;
  }
  .mascot .brand {
    display: block;
    margin-top: 6px;
    font-size: 23px;
    font-weight: 700;
    color: var(--ink-black);
    text-align: center;
    white-space: nowrap;
    letter-spacing: -0.5px;
  }
  .mascot.barrier { left: 76px; }
  .mascot.rigg { left: 240px; }
  .mascot.render { left: 410px; }
  .mascot.barrier .art { background: linear-gradient(135deg, var(--mascot-grey), var(--mascot-yellow) 55%, var(--mascot-blue)); }
  .mascot.rigg .art { background: linear-gradient(135deg, var(--mascot-yellow), var(--mascot-blue)); }
  .mascot.render .art { background: linear-gradient(135deg, var(--mascot-yellow) 40%, var(--mascot-blue) 80%, var(--mascot-grey)); }
  .divider {
    position: absolute;
    left: 592px;
    top: 525px;
    width: 4px;
    height: 209px;
    background: var(--divider);
    border-radius: 2px;
  }
  .company {
    position: absolute;
    top: 560px;
  }
  .company .dot {
    display: block;
    width: 60px;
    height: 60px;
    border-radius: 50%;
    margin-bottom: 22px;
  }
  .company .name {
    display: block;
    font-size: 31px;
    font-weight: 700;
    line-height: 30px;
    color: var(--ink-dark);
    letter-spacing: -1px;
    white-space: nowrap;
  }
  .company .tag {
    display: block;
    margin-top: 4px;
    font-size: 8px;
    color: var(--ink-light);
  }
  .company.structural { left: 637px; }
  .company.structural .dot { background: var(--mark-green); }
  .company.sealing { left: 838px; }
  .company.sealing .dot { background: var(--mark-blue); }
</style>
</head>
<body>
  <main class="signature">
    <p class="sign-off">Cheers,</p>

    <address class="details">
      <span class="line"><span class="name">First Last</span><span class="sep">I</span><span class="title">Job Title (Business)</span></span>
      <span class="line">24 Marlow Street, Hendon SA 5014</span>
      <span class="line"><span class="label">P:</span> XX XXXX XXXX<span class="sep">I</span><span class="label">F:</span> XX XXXX XXXX<span class="sep">I</span><span class="label">M:</span> XXXX XXX XXX</span>
      <span class="line"><span class="label">W:</span> www.domain.com.au<span class="sep">I</span>An Ardentis Group Company</span>
    </address>

    <div class="mascot barrier">
      <span class="art" role="img" aria-label="Cartoon builder mascot in hard hat standing beside a mesh fence panel"></span>
      <span class="brand">Mr. Barrier</span>
    </div>
    <div class="mascot rigg">
      <span class="art" role="img" aria-label="Cartoon builder mascot in hard hat holding a spanner beside scaffolding"></span>
      <span class="brand">Mr. Rigg</span>
    </div>
    <div class="mascot render">
      <span class="art" role="img" aria-label="Cartoon builder mascot in hard hat holding a trowel and plaster hawk"></span>
      <span class="brand">Mr. Render</span>
    </div>

    <div class="divider"></div>

    <div class="company structural">
      <span class="dot"></span>
      <span class="name">Ardentis<br>Structural</span>
      <span class="tag">An Ardentis Group Company</span>
    </div>
    <div class="company sealing">
      <span class="dot"></span>
      <span class="name">Keystone<br>Sealing Services</span>
      <span class="tag">An Ardentis Group Company</span>
    </div>
  </main>
</body>
</html>
```